Email Signature

Our company is having its 10th anniversary in 2021. We would like a new email signature to celebrate the occasion. Attached is our business card design.
Please refer to our website for actual contact details.
www.tarvinestates.com.au

Industry/Entity Type

Real Estate

Requirements
Must have
• Our logo
Email
Contact Numbers
Address
Website address

Celebrating 10 years in 2021
Nice to have
• Something that blends the designs of our website and business card

```html
<!DOCTYPE html>
<html lang="en">
<head>
<meta charset="utf-8">
<title>Tarvin Estates – Email Signature</title>
<link href="https://fonts.googleapis.com/css2?family=Exo+2:wght@400;600;700&family=Roboto:wght@400&display=swap" rel="stylesheet">
<style>
  :root {
    --backdrop: #e2c5b9;
    --card: #ffffff;
    --card-edge: #4a4a4a;
    --brand-blue: #1f64a8;
    --brand-navy: #1c2f4f;
    --ink: #333333;
    --muted: #5c5c5c;
    --rule: #c9c9c9;
    --banner-white: #ffffff;
  }
  * { box-sizing: border-box; margin: 0; padding: 0; }
  html, body {
    width: 1200px; height: 1200px; overflow: hidden;
    background: var(--backdrop);
  }
  .signature {
    position: absolute;
    left: 53px; top: 402px;
    width: 1094px; height: 396px;
    background: var(--card);
    border: 1px solid var(--card-edge);
    font-family: "Roboto", Arial, sans-serif;
  }
  .brand {
    position: absolute;
    left: 74px; top: 90px;
    width: 290px; height: 130px;
    display: flex; align-items: center; gap: 14px;
  }
  .brand-mark {
    width: 26px; height: 26px;
    background: var(--brand-blue);
    flex: none;
  }
  .brand-name {
    font-family: "Exo 2", Arial, sans-serif;
    font-weight: 700;
    font-size: 31px;
    line-height: 1.05;
    color: var(--brand-navy);
    letter-spacing: 0.5px;
  }
  .divider {
    position: absolute;
    left: 382px; top: 74px;
    width: 1px; height: 162px;
    background: var(--rule);
  }
  .details {
    position: absolute;
    left: 410px; top: 52px;
    width: 600px;
  }
  .person-name {
    font-family: "Exo 2", Arial, sans-serif;
    font-weight: 600;
    font-size: 26px;
    color: var(--brand-blue);
    line-height: 1.1;
  }
  .person-role {
    font-size: 18px;
    color: var(--muted);
    margin-top: 3px;
  }
  .contact {
    margin-top: 15px;
    font-size: 16.5px;
    letter-spacing: 1.6px;
    color: var(--ink);
    line-height: 21px;
    white-space: nowrap;
  }
  .contact .label { color: var(--brand-blue); }
  .address {
    margin-top: 12px;
    font-size: 16.5px;
    letter-spacing: 1.6px;
    color: var(--ink);
    padding-bottom: 9px;
    border-bottom: 1px solid var(--rule);
    width: 464px;
    white-space: nowrap;
  }
  .social {
    display: flex; gap: 5px;
    margin-top: 9px;
  }
  .social-dot {
    width: 24px; height: 24px; border-radius: 50%;
    background: var(--brand-blue);
  }
  .banner {
    position: absolute;
    left: 72px; top: 259px;
    width: 950px; height: 84px;
    background: linear-gradient(90deg, #d9c0bb 0%, #cfc3c9 40%, #5a6f9a 58%, #2d3f70 75%, #c98a64 100%);
  }
  .banner-tagline,
  .banner-name {
    position: absolute;
    top: 19px; height: 50px;
    display: flex; align-items: center; justify-content: center;
    font-family: "Exo 2", Arial, sans-serif;
    font-weight: 400;
    white-space: nowrap;
    overflow: hidden;
  }
  .banner-tagline {
    left: 15px; width: 593px;
    background: var(--banner-white);
    font-size: 30px;
    letter-spacing: 2px;
    color: var(--brand-blue);
  }
  .banner-name {
    left: 632px; width: 294px;
    background: var(--brand-blue);
    font-size: 28px;
    letter-spacing: 1px;
    color: #ffffff;
  }
</style>
</head>
<body>
  <section class="signature">
    <div class="brand">
      <span class="brand-mark"></span>
      <span class="brand-name">TARVIN<br>ESTATES</span>
    </div>
    <div class="divider"></div>
    <div class="details">
      <p class="person-name">Daniel K. Marlowe</p>
      <p class="person-role">Owner</p>
      <p class="contact"><span class="label">T :</span> 1300 00TARV(8278) | <span class="label">F:</span> 9015 4882<br><span class="label">E :</span> admin@tarvinestates.com.au | <span class="label">W :</span> www.tarvinestates.com.au</p>
      <p class="address">Shop 2 / 18 Harbourview Road, Meadowbank, NSW 2114</p>
      <div class="social">
        <span class="social-dot"></span>
        <span class="social-dot"></span>
      </div>
    </div>
    <div class="banner" role="img" aria-label="Photograph of a modern two-storey home at dusk">
      <div class="banner-tagline">CELEBRATING 10 YEARS IN 2021</div>
      <div class="banner-name">TARVIN ESTATES</div>
    </div>
  </section>
</body>
</html>
```